The task involves the design and creation of a wordpress website for plainpactly.co.
Plainpactly.co is a website through which people can purchase template legal contracts.The website is focused on Australian users although in the future we may target users in other countries.
*************************************************
We will offer 3 bundles of products (a small business, medium business and a large business bundle) as follows:
(a) a Starter package ($199);
(b) a Pro (professional) package ($499);
(c) an Enterprise package ($1,500).
Each bundle contains a number of legal templates. The Pro package includes all of the legal templates in the Starter package. The Enterprise version contains all the legal templates in the Starter and Pro package.
The starter bundle will include the following legal documents:
+Website terms and conditions
+Confidentiality agreement
+Services agreement
+Purchase order terms and conditions
+Variation agreement
+Independent contractor agreement
+Term sheet
The Pro bundle includes:
+ all of the documents contained in the Starter package plus
+ Request for tender
+ Consultancy agreement
+ Contract labour agreement
+ Sponsorship agreement
The Enterprise package includes:
+All of the documents in our Pro package plus
+Freight Services agreement
+IT Services agreement
+Website design and hosting agreement
+Teaming agreement
+Long form services agreement
+Distribution agreement
+Content supply agreement
****************************************************
We like the simplicity and layout of the following websites:
http://leavewatchr.com/
https://www.trygleanly.com/
http://www.fornavo.com/
http://www.quillrule.com/
http://usebrimo.com/
We like the way on the leavewatchr.com page when you click on the pricing tab and other tabs of the navigation bar you are taken lower down on the homepage to the content. We like the static header on leavewatchr and Fornavo. We also like the use of big headings, images and symbols to convey meaning as well as having the webpage broken into sections.
We will want an email sign up capability and will need to integrate an email collection capability with postwren or similar.
We like the way it is referred to on the https://www.ledgerpleader.com/ website where it says:
"Your first document is free" and them there is an email sign up box.
We imagine having a similar features at a couple of places on the site with a call to action.
We also imagine including some sort of website abandonment application similar to http://leavewatchr.com/ or http://stayhold.com/. We would also like a countdown clock linked to a discount off the price of the bundles. Please provide a recommendation and ensure that this can easily be integrated.
We will need an e-commence capability so that we can sell our products.
******************************************
Our value proposition is as follows:
1. Lower your legal costs by using our template documents as a starting point
Why pay a lawyer to create a document from scratch when you can you our template agreements as the starting point.
2. Variety of bundles to chose from
We offer you the opportunity to purchase the bundle of documents that are just right for you – small business, medium business and large business options.
3.Customise agreements yourself or have your lawyer customise them for you.
Our contracts are drafted in plain English and you can provide them to your lawyer and ask them to customise them for you.
4. Reviewed by top lawyers - customised for Australia
All of our legal documents have been reviewed by a lawyer with experience working at a top international law firm.
***************************************************
The benefits of the service are:
* Documents reviewed by Australian lawyer with experience at top tier Australian law firm.
* Cost effective approach to risk management
* Electronic delivery
* Use templates as often as you like for your internal business purposes
* Free explanation of each template agreement
* Sensible approach to legal drafting to minimise contract negotiation time
*****************************************************
We will need to include the following across the bottom of each webpage.
"Copyright 2014 PlainPactly. All rights reserved. PlainPactly provides information only. PlainPactly is not a "lawyer referral service" and does not provide legal advice or participate in any legal representation. PlainPactly is not a law firm or a substitute for a qualified lawyer or law firm. For legal advice, please contact a lawyer. Use of PlainPactly.co is subject to our Terms and Conditions."
The reference to Terms and Conditions will be a link to the Terms and Conditions.
*********************************************************
The Contact Us section should be a simple webform. We will not include any telephone or physical address at this stage.
For the About Us section
We can include the following:
PlainPactly was conceived and nurtured in Melbourne, the world's most liveable city by an experienced lawyer who loves the idea of making legal contracting affordable for small and medium size businesses. We have friends in other cities who help make PlainPactly possible.
************************************************************
We expect the website created to be user friendly, able to be updated easily, optimised for search engines and to be built on wordpress. The website should be able to integrate with third party applications (eg analytic software, email marketing tools etc). Please include recommendations for third party software for integration. We have installed Wordpress 3.9.
Target Market(s)
Small to medium business owners.

```html
<!DOCTYPE html>
<html lang="en">
<head>
<meta charset="utf-8">
<title>PlainPactly – Lower your legal costs</title>
<link href="https://fonts.googleapis.com/css2?family=Open+Sans:wght@300;400;600;700&display=swap" rel="stylesheet">
<style>
:root{
  --red:#e6493b;
  --red-band:#ee514a;
  --red-dark:#c23a2e;
  --ink:#333333;
  --ink-soft:#555555;
  --white:#ffffff;
  --card:#f2f2f2;
  --btn-dark:#3b3b3b;
  --footer:#e1e1e1;
  --bar:#3a3a3a;
  --rule:#bbbbbb;
}
*{box-sizing:border-box;margin:0;padding:0}
html,body{width:1200px;height:2296px;overflow:hidden}
body{font-family:"Open Sans",Arial,sans-serif;color:var(--ink);background:var(--white);position:relative}
section,header,footer{position:relative;width:1200px;overflow:hidden}
.abs{position:absolute}

/* header */
.site-header{height:59px;background:var(--red)}
.brand{left:158px;top:12px;display:flex;align-items:center;gap:10px;color:var(--white);font-size:27px;font-weight:400}
.brand-mark{width:28px;height:28px;background:var(--white);border-radius:3px}
.utility-nav{top:10px;left:722px;display:flex;gap:22px;font-size:9.5px;letter-spacing:1px;color:var(--white);text-transform:uppercase}
.search-btn{left:1004px;top:6px;width:24px;height:24px;background:var(--red-dark);border-radius:2px}
.main-nav{top:35px;left:0;width:1200px;font-size:13px;color:var(--white)}
.main-nav span{position:absolute;white-space:nowrap}
.main-nav .active::after{content:"";position:absolute;left:-2px;right:-2px;top:21px;height:3px;background:var(--bar)}

/* hero */
.hero{height:356px;background:linear-gradient(90deg,#d9d6d2 0%,#cfc9c3 40%,#8a7f76 70%,#c6bcb2 100%)}
.hero-photo{inset:0}
.hero-title{left:179px;top:80px;font-size:50px;font-weight:300;color:#111}
.hero-sub{left:187px;top:146px;font-size:21px;color:#111}
.hero-sub b{font-weight:700}
.hero-btn{left:342px;top:198px;width:127px;height:44px;background:var(--red);color:var(--white);font-size:13px;display:flex;align-items:center;justify-content:center;box-shadow:0 3px 0 var(--red-dark)}

/* section title */
.sec-title{left:0;width:1200px;text-align:center;font-weight:300}
.divider{left:519px;width:162px;height:1px;background:var(--rule)}
.divider::after{content:"";position:absolute;left:77px;top:-3px;width:7px;height:7px;border:1px solid var(--rule);border-radius:50%;background:var(--white)}

/* value propositions */
.values{height:324px}
.values .sec-title{top:20px;font-size:36px;color:var(--red)}
.values .sec-title b{font-weight:600}
.values .divider{top:80px}
.vp-icon{width:34px;height:34px;border-radius:50%;background:var(--red)}
.vp-text{width:310px;font-size:12px;line-height:18px;color:var(--ink)}
.vp-text h3{font-size:12px;font-weight:400;color:var(--red);margin-bottom:2px}

/* plans */
.plans{height:618px;background:var(--red-band);color:var(--white)}
.plans .sec-title{top:10px;font-size:35px;color:var(--white)}
.plans-label{left:462px;top:58px;width:276px;height:20px;background:#111;color:var(--white);font-size:12px;text-align:center;line-height:20px}
.plan-card{top:103px;width:263px;height:432px;background:var(--card);color:var(--ink);box-shadow:0 3px 0 #d9d9d9;text-align:center}
.plan-name{margin-top:14px;font-size:20px;font-weight:300;line-height:26px;text-transform:uppercase}
.plan-note{font-size:11.5px;margin-top:2px}
.plan-price{font-size:31px;color:var(--red);margin-top:8px}
.plan-list{list-style:none;text-align:left;margin:20px 0 0 14px;font-size:13px;line-height:25px}
.plan-list li::before{content:"• ";color:#222}
.plan-buy{left:44px;top:358px;width:170px;height:46px;background:var(--btn-dark);color:var(--white);font-size:13px;display:flex;align-items:center;justify-content:center;box-shadow:0 3px 0 #111}
.plans-note{left:158px;top:560px;width:890px;font-size:12px;line-height:18px}

/* benefits */
.benefits{height:223px;border-bottom:2px solid var(--red)}
.benefits .sec-title{top:12px;font-size:22px;color:var(--ink)}
.benefits .sec-title b{font-weight:700}
.benefits .divider{top:54px}
.benefit-icon{width:34px;height:34px}
.benefit-text{width:200px;font-size:11.5px;line-height:17px;color:var(--ink)}

/* newsletter */
.newsletter{height:200px;background:var(--red-band);color:var(--white)}
.news-box{left:242px;top:21px;width:716px;height:158px;border:1px dashed rgba(255,255,255,.85)}
.newsletter .sec-title{top:27px;font-size:34px;color:var(--white)}
.newsletter .sec-title b{font-weight:600}
.news-note{left:0;width:1200px;top:80px;text-align:center;font-size:11px}
.newsletter .divider{top:100px;background:rgba(255,255,255,.8)}
.newsletter .divider::after{background:var(--red-band);border-color:var(--white)}
.news-input{left:264px;top:114px;width:486px;height:46px;background:var(--white);border-radius:2px}
.news-btn{left:765px;top:114px;width:169px;height:46px;background:var(--btn-dark);color:var(--white);font-size:13px;display:flex;align-items:center;justify-content:center;box-shadow:0 3px 0 #111}

/* contact */
.contact{height:357px}
.contact-art{left:158px;top:41px;width:317px;height:293px;border-radius:50%;background:radial-gradient(circle,#e9c9a8 0%,#cfcfcf 45%,#bdbdbd 70%,var(--white) 71%)}
.contact .sec-title{left:567px;width:478px;top:10px;font-size:35px;color:var(--red)}
.contact .sec-title b{font-weight:600}
.contact-note{left:603px;top:74px;width:401px;height:19px;background:#7a7a7a;color:var(--white);font-size:11.5px;text-align:center;line-height:19px}
.field{height:30px;border:1px solid #cfcfcf;border-radius:3px;font-size:11px;color:#555;padding:7px 14px}
.field.msg{height:89px}
.send-btn{left:717px;top:287px;width:171px;height:44px;background:var(--red);color:var(--white);font-size:13px;display:flex;align-items:center;justify-content:center;box-shadow:0 3px 0 var(--red-dark)}

/* footer */
.site-footer{height:114px;background:var(--footer)}
.foot-brand{left:163px;top:40px;display:flex;align-items:center;gap:10px;font-size:20px;font-weight:300;color:#8a8a8a}
.foot-brand span.sq{width:26px;height:26px;border:2px solid #a9a9a9;border-radius:3px}
.foot-col h4{font-size:13px;font-weight:400;text-transform:uppercase;color:#333;margin-bottom:10px;white-space:nowrap}
.foot-col p{font-size:11px;line-height:25px;color:#333}
.social{top:52px;width:18px;height:18px;background:var(--red)}
.legal-bar{height:45px;background:var(--bar);color:var(--white);font-size:8.5px;line-height:13px;padding:9px 0 0 149px}
.legal-bar p{width:1040px}
.legal-bar a{color:var(--white);text-decoration:none}
</style>
</head>
<body>

<header class="site-header">
  <div class="brand abs"><span class="brand-mark"></span>PlainPactly</div>
  <nav class="utility-nav abs"><span>Login</span><span>Register</span><span>Your Cart</span><span>Checkout</span></nav>
  <div class="search-btn abs">
    <svg width="24" height="24" viewBox="0 0 24 24"><circle cx="11" cy="10" r="5" fill="none" stroke="#fff" stroke-width="2"/><line x1="7.5" y1="13.5" x2="4" y2="18" stroke="#fff" stroke-width="2"/></svg>
  </div>
  <nav class="main-nav abs">
    <span class="active" style="left:583px">Home</span>
    <span style="left:660px">Pricing</span>
    <span style="left:741px">Value Propositions</span>
    <span style="left:887px">Benefits</span>
    <span style="left:970px">Contact us</span>
  </nav>
</header>

<section class="hero">
  <div class="hero-photo abs" role="img" aria-label="Photo of a smiling man working on a laptop in a bright office"></div>
  <h1 class="hero-title abs">Lower your legal costs</h1>
  <p class="hero-sub abs">by using our template documents <b>as a starting point.</b></p>
  <a class="hero-btn abs">Get the Pricing!</a>
</section>

<section class="values">
  <h2 class="sec-title abs">Our <b>Value Propositions</b></h2>
  <div class="divider abs"></div>

  <div class="vp-icon abs" style="left:186px;top:112px"></div>
  <div class="vp-text abs" style="left:241px;top:111px">
    <h3>1. Lower your legal costs by using our template documents as a starting point.</h3>
    Why pay a lawyer to create a document from scratch when you can you our template agreements as the starting point.
  </div>

  <div class="vp-icon abs" style="left:682px;top:112px"></div>
  <div class="vp-text abs" style="left:733px;top:111px">
    <h3>2. Variety of bundles to chose from.</h3>
    We offer you the opportunity to purchase the bundle of documents that are just right for you – small business, medium business and large business options.
  </div>

  <div class="vp-icon abs" style="left:186px;top:213px"></div>
  <div class="vp-text abs" style="left:241px;top:212px">
    <h3>3. Customise agreements yourself or have your lawyer customise them for you.</h3>
    Our contracts are drafted in plain English and you can provide them to your lawyer and ask them to customise them for you.
  </div>

  <div class="vp-icon abs" style="left:682px;top:213px"></div>
  <div class="vp-text abs" style="left:733px;top:212px">
    <h3>4. Reviewed by top lawyers - customised for Australia.</h3>
    All of our legal documents have been reviewed by a lawyer with experience working at a top international law firm.
  </div>
</section>

<section class="plans">
  <h2 class="sec-title abs">Browse Our Plans</h2>
  <div class="plans-label abs">Please choose a plan from below and proceed</div>

  <article class="plan-card abs" style="left:185px">
    <h3 class="plan-name">Starter</h3>
    <p class="plan-note">bundle includes:</p>
    <p class="plan-price">$199</p>
    <ul class="plan-list">
      <li>Website terms and conditions</li>
      <li>Confidentiality agreement</li>
      <li>Services agreement</li>
      <li>Purchase order terms and conditions</li>
      <li>Variation agreement</li>
      <li>Independent contractor agreement</li>
      <li>Term sheet</li>
    </ul>
    <a class="plan-buy abs">Buy Now</a>
  </article>

  <article class="plan-card abs" style="left:471px">
    <h3 class="plan-name">The Pro<br>(Professional)</h3>
    <p class="plan-note">bundle includes:</p>
    <p class="plan-price">$499</p>
    <ul class="plan-list" style="line-height:19px;margin-top:24px">
      <li style="margin-bottom:6px">All of the documents contained in<br>&nbsp;&nbsp;the Starter package plus</li>
      <li style="margin-bottom:6px">Request for tender</li>
      <li style="margin-bottom:6px">Consultancy agreement</li>
      <li style="margin-bottom:6px">Contract labour agreement</li>
      <li>Sponsorship agreement</li>
    </ul>
    <a class="plan-buy abs">Buy Now</a>
  </article>

  <article class="plan-card abs" style="left:757px">
    <h3 class="plan-name">The Enterprise</h3>
    <p class="plan-note">bundle includes:</p>
    <p class="plan-price">$1,500</p>
    <ul class="plan-list" style="margin-left:12px">
      <li style="line-height:18px;margin-bottom:5px">All of the documents in our Pro<br>&nbsp;&nbsp;package plus</li>
      <li>Freight Services agreement</li>
      <li>IT Services agreement</li>
      <li>Website design and hosting agreement</li>
      <li>Teaming agreement</li>
      <li>Long form services agreement</li>
      <li>Distribution agreement</li>
      <li>Content supply agreement</li>
    </ul>
    <a class="plan-buy abs">Buy Now</a>
  </article>

  <p class="plans-note abs">Each bundle contains a number of legal templates. The Pro package includes all of the legal templates in the Starter package. The Enterprise version contains all the legal templates in the Starter and Pro package.</p>
</section>

<section class="benefits">
  <h2 class="sec-title abs"><b>THE BENEFITS</b> OF THE SERVICE ARE:</h2>
  <div class="divider abs"></div>

  <svg class="benefit-icon abs" style="left:155px;top:88px" viewBox="0 0 34 34"><circle cx="17" cy="17" r="14" fill="#111"/></svg>
  <p class="benefit-text abs" style="left:207px;top:88px">Documents reviewed by Australian lawyer with experience at top tier Australian law firm.</p>

  <svg class="benefit-icon abs" style="left:492px;top:88px" viewBox="0 0 34 34"><circle cx="17" cy="17" r="15" fill="#111"/><circle cx="17" cy="17" r="11" fill="none" stroke="#fff" stroke-width="1.5"/><text x="17" y="23" text-anchor="middle" font-family="Open Sans,sans-serif" font-weight="700" font-size="16" fill="#fff">$</text></svg>
  <p class="benefit-text abs" style="left:540px;top:88px">Cost effective approach to risk management.</p>

  <svg class="benefit-icon abs" style="left:808px;top:88px" viewBox="0 0 34 34"><rect x="5" y="6" width="24" height="17" fill="none" stroke="#111" stroke-width="2.5"/><rect x="1" y="25" width="32" height="3" fill="#111"/></svg>
  <p class="benefit-text abs" style="left:867px;top:88px">Electronic delivery.</p>

  <svg class="benefit-icon abs" style="left:161px;top:168px" viewBox="0 0 34 34"><rect x="5" y="2" width="24" height="30" rx="3" fill="none" stroke="#111" stroke-width="3"/><line x1="10" y1="11" x2="24" y2="11" stroke="#111" stroke-width="2.5"/><line x1="10" y1="17" x2="24" y2="17" stroke="#111" stroke-width="2.5"/><line x1="10" y1="23" x2="24" y2="23" stroke="#111" stroke-width="2.5"/></svg>
  <p class="benefit-text abs" style="left:207px;top:168px">Use templates as often as you like for your internal business purposes.</p>

  <svg class="benefit-icon abs" style="left:491px;top:168px" viewBox="0 0 34 34"><ellipse cx="13" cy="13" rx="12" ry="9" fill="#111"/><path d="M5 19 L3 26 L11 21Z" fill="#111"/><ellipse cx="23" cy="22" rx="10" ry="7.5" fill="#111" stroke="#fff" stroke-width="1.5"/><path d="M28 27 L31 32 L24 29Z" fill="#111"/></svg>
  <p class="benefit-text abs" style="left:540px;top:168px">Free explanation of each template agreement.</p>

  <svg class="benefit-icon abs" style="left:810px;top:168px" viewBox="0 0 34 34"><path d="M6 10 A13 13 0 1 1 5 21" fill="none" stroke="#111" stroke-width="3"/><path d="M2 6 L8 12 L1 13Z" fill="#111"/><path d="M17 9 V18 L23 22" fill="none" stroke="#111" stroke-width="3"/></svg>
  <p class="benefit-text abs" style="left:867px;top:168px">Sensible approach to legal drafting to minimise contract negotiation time.</p>
</section>

<section class="newsletter">
  <div class="news-box abs"></div>
  <h2 class="sec-title abs">Subscribe to <b>Our Free Newsletter</b></h2>
  <p class="news-note abs">* Your first document is FREE</p>
  <div class="divider abs"></div>
  <div class="news-input abs"></div>
  <a class="news-btn abs">Grab The Plan</a>
</section>

<section class="contact">
  <div class="contact-art abs" role="img" aria-label="Illustration of a handshake surrounded by business icons: target, envelope, globe, gears and chat bubble"></div>
  <h2 class="sec-title abs">Send us <b>a Quick Message</b></h2>
  <p class="contact-note abs">Please fillup the form below and submit us your query.</p>
  <div class="field abs" style="left:567px;top:107px;width:226px">Your Name</div>
  <div class="field abs" style="left:818px;top:107px;width:227px">Your Email</div>
  <div class="field abs" style="left:567px;top:142px;width:478px">Subject</div>
  <div class="field msg abs" style="left:567px;top:177px;width:478px">Message</div>
  <a class="send-btn abs">Send Message</a>
</section>

<footer class="site-footer">
  <div class="foot-brand abs"><span class="sq"></span>PlainPactly</div>
  <div class="foot-col abs" style="left:418px;top:14px"><h4>Quick Links</h4><p>Plans<br>Value propositions</p></div>
  <div class="foot-col abs" style="left:586px;top:14px"><h4>Legal</h4><p>Terms of Use<br>Privacy Policy</p></div>
  <div class="foot-col abs" style="left:728px;top:14px"><h4>Extras</h4><p>Benefits<br>Contact Us</p></div>
  <div class="foot-col abs" style="left:847px;top:14px"><h4>Get Connected</h4></div>
  <span class="social abs" style="left:853px"></span>
  <span class="social abs" style="left:882px"></span>
  <span class="social abs" style="left:911px"></span>
  <span class="social abs" style="left:940px"></span>
  <span class="social abs" style="left:969px"></span>
</footer>
<div class="legal-bar">
  <p>© 2014 PlainPactly. All rights reserved. PlainPactly provides information only. PlainPactly is not a "lawyer referral service" and does not provide legal advice or participate in any legal representation. PlainPactly is not a law firm or a substitute for a qualified lawyer or law firm. For legal advice, please contact a lawyer. Use of PlainPactly.co is subject to our <a>Terms and Conditions</a>.</p>
</div>

</body>
</html>
```